Crumb Crumb - Home baking business needs a business card design. I sell at artisan food festivals.

A design for rebranding my baking business which serves artisan food festivals in the UK. Produce is locally sourced, homegrown or foraged, I make rustic unusual recipes. I would like a simple design using classic colours. I like green, 'Hadley and Stone". I like chunky lettering, but very open to new ideas/designs. On the reverse side I would like a singular symbol demonstrating baking either a bowl and wooden spoon or cake and the facebook icon with CrumbCrumb
Updates

Project Deadline Extended
Reason: I would like to progress with the design by Jen Marlow 4827306 . I misunderstood the deadline itinerary but would very much like to go ahead with your design. thanks

Target Market(s)

customers at food festivals, other small food businesses

Industry/Entity Type

Business

Contact Information for Business Card

Minimal amount of type on the card. Design to accentuate the look of my stall and style of baking . I display cakes on either old slate tiles, old palette boxes. Prices are hand written on brown luggage labels

Font styles to use
Other font styles liked:
• Blair MdiTC

Requirements
Must have
• Underneath Crumb Crumb i would like to have homemade by Pam somewhere on the front of the card.
Nice to have
• Clear lettering, classic colours i.e. Hadley and Stone colour palettes.
Should not have
• Fancy, blingy, wordy,

```html
<!DOCTYPE html>
<html lang="en">
<head>
<meta charset="utf-8">
<title>Crumb Crumb – Business Card</title>
<link href="https://fonts.googleapis.com/css2?family=Noto+Serif:ital,wght@0,300;0,400;1,300&family=Montserrat:wght@700&family=Courier+Prime&display=swap" rel="stylesheet">
<style>
  :root {
    --page-bg: #ece9e2;
    --leaf-light: #b9df5c;
    --leaf-mid: #9ccd45;
    --leaf-dark: #79ad2c;
    --band-white: #f4f4f2;
    --ink: #1c1c1c;
    --soft-ink: #4a4a4a;
    --contact-ink: #d8efa6;
    --mark-light: #dcefb4;
    --mark-mid: #b9df5c;
    --shadow: rgba(40, 50, 20, 0.28);
  }
  * { margin: 0; padding: 0; box-sizing: border-box; }
  html, body { width: 1200px; height: 780px; overflow: hidden; }
  body {
    background: var(--page-bg);
    display: flex;
    align-items: center;
    justify-content: center;
    gap: 48px;
  }
  .card {
    position: relative;
    width: 540px;
    height: 309px;
    border-radius: 3px;
    overflow: hidden;
    background: radial-gradient(ellipse at 60% 45%, var(--leaf-light) 0%, var(--leaf-mid) 55%, var(--leaf-dark) 100%);
    box-shadow: 0 10px 26px var(--shadow);
  }
  .card-art { position: absolute; inset: 0; }
  .wordmark {
    position: absolute;
    font-family: "Noto Serif", serif;
    font-weight: 300;
    color: var(--ink);
    letter-spacing: 1px;
    line-height: 1;
  }
  .front .wordmark { font-size: 40px; top: 52px; }
  .front .wordmark.left { left: 34px; }
  .front .wordmark.right { left: 330px; }
  .tagline {
    position: absolute;
    left: 332px;
    top: 98px;
    font-family: "Noto Serif", serif;
    font-weight: 300;
    font-size: 12px;
    letter-spacing: 1px;
    color: var(--soft-ink);
    line-height: 1;
  }
  .back .wordmark { font-size: 46px; top: 128px; }
  .back .wordmark.left { left: 40px; }
  .back .wordmark.right { right: 40px; }
  .contact {
    position: absolute;
    left: 178px;
    top: 166px;
  }
  .contact .name {
    font-family: "Montserrat", sans-serif;
    font-weight: 700;
    font-size: 17px;
    color: var(--ink);
    letter-spacing: 0.5px;
  }
  .contact .role,
  .contact .line {
    font-family: "Courier Prime", monospace;
    font-size: 13px;
    color: var(--contact-ink);
  }
  .contact .role { margin-top: 1px; }
  .contact .details { margin-top: 22px; line-height: 1.45; }
</style>
</head>
<body>

  <section class="card front" aria-label="Business card front">
    <svg class="card-art" width="540" height="309" viewBox="0 0 540 309">
      <defs>
        <radialGradient id="markToneFront" cx="50%" cy="50%" r="50%">
          <stop offset="0%" stop-color="var(--mark-light)"/>
          <stop offset="100%" stop-color="var(--mark-mid)"/>
        </radialGradient>
      </defs>
      <rect x="0" y="40" width="540" height="80" fill="var(--band-white)"/>
      <circle cx="230" cy="80" r="66" fill="var(--band-white)"/>
      <path d="M0,40 L177.5,40 A66,66 0 0 1 282.5,40 L540,40" fill="none" stroke="var(--ink)" stroke-width="2"/>
      <path d="M0,120 L177.5,120 A66,66 0 0 0 282.5,120 L540,120" fill="none" stroke="var(--ink)" stroke-width="2"/>
      <circle class="mark-area" cx="230" cy="80" r="40" fill="url(#markToneFront)" role="img" aria-label="Bakery symbol area"/>
    </svg>
    <span class="wordmark left">Crumb</span>
    <span class="wordmark right">Crumb</span>
    <span class="tagline">homemade by Pam</span>
    <div class="contact">
      <p class="name">EMPLOYEE NAME</p>
      <p class="role">Managing Director</p>
      <div class="details">
        <p class="line">0012 3456 789</p>
        <p class="line">info@youremail.com</p>
      </div>
    </div>
  </section>

  <section class="card back" aria-label="Business card back">
    <svg class="card-art" width="540" height="309" viewBox="0 0 540 309">
      <defs>
        <radialGradient id="markToneBack" cx="50%" cy="50%" r="50%">
          <stop offset="0%" stop-color="var(--mark-light)"/>
          <stop offset="100%" stop-color="var(--mark-mid)"/>
        </radialGradient>
      </defs>
      <rect x="0" y="112" width="540" height="85" fill="var(--band-white)"/>
      <circle cx="270" cy="154.5" r="70" fill="var(--band-white)"/>
      <path d="M0,112 L214.4,112 A70,70 0 0 1 325.6,112 L540,112" fill="none" stroke="var(--ink)" stroke-width="2"/>
      <path d="M0,197 L214.4,197 A70,70 0 0 0 325.6,197 L540,197" fill="none" stroke="var(--ink)" stroke-width="2"/>
      <circle class="mark-area" cx="270" cy="154.5" r="44" fill="url(#markToneBack)" role="img" aria-label="Bakery symbol area"/>
    </svg>
    <span class="wordmark left">Crumb</span>
    <span class="wordmark right">Crumb</span>
  </section>

</body>
</html>
```